Tea Kanoseki Matcha packaging. Matcha from Japan, by Japanese.

Our company, Kanosekiworks.co.jp is a company steeped in Japanese traditional festival products for nearly 100 years. Located in Yame, Japan's famous tea region. We now create a new branch in our business, starting with matcha.

We need a contemporary yet reflect the tradition of our products design for matcha packaging. This design is aimed at young US consumer.

We will have 6 different types of matcha, each at different grade and price point. We would like to use colour and product name to differentiate between them. Product name shall include the grade of matcha: culinary, premium or ceremonial; and a Japanese name such as Somaru, Tonebi ...; and a short description blended matcha or first harvest from either Uji, Kagoshima or Yame region.

The design should have information panel at the back for US market. Please refer to the sample design in the attachment.

Size of matcha pouch
2 sizes
12 x 15 cm
12 x 19.5cm

Please note the logo can be custom and change to fit the design. But it must have Kanoseki's family crest on it, with or without the circle.

Target Market(s)

US market

Industry/Entity Type

Food and Drink

Requirements
Must have
• As we have 6 different matcha, they shall be somehow differentiated between them, possibly by colour.
Nice to have
• As our company traditionally making Kabuto, Hina Ningyo ...., if you can include a mas

```html
<!DOCTYPE html>
<html lang="en">
<head>
<meta charset="utf-8">
<title>Tea Kanoseki Matcha – Grade Range</title>
<link rel="stylesheet" href="https://fonts.googleapis.com/css2?family=Playfair+Display:wght@700;800&family=Red+Hat+Display:wght@300;500;700;800&family=Noto+Serif+SC:wght@400&display=swap">
<style>
  :root {
    --backdrop: #ececec;
    --pouch: #ffffff;
    --ink: #1b1b1b;
    --culinary: #a07f08;
    --premium: #163a24;
    --ceremonial: #3d0e0e;
    --grade-green: #163a24;
    --leaf-light: #a9cf5a;
    --leaf-mid: #4f9a2a;
    --leaf-dark: #1f5a16;
    --badge-green: #3a8a3a;
  }
  * { margin: 0; padding: 0; box-sizing: border-box; }
  html, body { width: 1200px; height: 638px; overflow: hidden; background: var(--backdrop); }
  .range { position: relative; width: 1200px; height: 638px; }

  .pouch {
    position: absolute; top: 53px; width: 340px; height: 553px;
    background: var(--pouch);
    box-shadow: 0 8px 10px -6px rgba(0,0,0,0.18);
    overflow: hidden;
  }
  .pouch--culinary { left: 57px; --accent: var(--culinary); --grade-ink: var(--ink); }
  .pouch--premium { left: 428px; --accent: var(--premium); --grade-ink: var(--premium); }
  .pouch--ceremonial { left: 797px; --accent: var(--ceremonial); --grade-ink: var(--grade-green); }

  .leaf-art {
    position: absolute; left: 0; top: 42px; width: 205px; height: 248px;
    background: radial-gradient(ellipse at 35% 45%, var(--leaf-mid) 0%, var(--leaf-dark) 45%, transparent 72%),
                linear-gradient(160deg, var(--leaf-dark) 0%, var(--leaf-mid) 55%, var(--leaf-light) 100%);
    border-radius: 0 60% 40% 0 / 0 55% 45% 0;
    opacity: 0.9;
  }

  .brand { position: absolute; left: 96px; top: 28px; width: 150px; text-align: center; }
  .brand__mark {
    display: block; margin: 0 auto 8px; width: 56px; height: 56px;
    border-radius: 50%; background: var(--ink);
  }
  .brand__name {
    font-family: "Playfair Display", serif; font-weight: 800;
    font-size: 17px; letter-spacing: 0.3px; color: var(--ink); white-space: nowrap;
  }

  .verse {
    position: absolute; font-family: "Noto Serif SC", serif;
    writing-mode: vertical-rl; color: var(--accent); line-height: 1;
  }
  .verse--main { left: 243px; top: 80px; font-size: 37px; letter-spacing: 4px; }
  .verse--side { left: 285px; top: 124px; font-size: 31px; letter-spacing: 3px; }

  .grade {
    position: absolute; right: 24px; top: 342px;
    font-family: "Red Hat Display", sans-serif; font-weight: 800;
    font-size: 21px; letter-spacing: 0.5px; color: var(--grade-ink);
  }

  .uses {
    position: absolute; right: 242px; top: 456px; text-align: right;
    font-family: "Red Hat Display", sans-serif; font-weight: 500;
    font-size: 8.6px; line-height: 12px; color: var(--ink);
  }

  .badges { position: absolute; left: 5px; top: 499px; display: flex; gap: 3px; align-items: center; }
  .badge--round { width: 19px; height: 19px; border-radius: 50%; border: 2px solid var(--badge-green); }
  .badge--oval { width: 30px; height: 19px; border-radius: 10px; border: 2px solid var(--badge-green); }
  .badge--plate { width: 42px; height: 16px; background: var(--ink); }

  .label {
    position: absolute; left: 102px; top: 372px; width: 238px; height: 147px;
    background: var(--accent); color: #fff;
    font-family: "Red Hat Display", sans-serif;
  }
  .label__name {
    position: absolute; left: 10px; top: 10px;
    font-weight: 300; font-size: 26px; line-height: 29px; letter-spacing: 0.3px;
  }
  .label__tagline {
    position: absolute; left: 11px; top: 103px;
    font-weight: 300; font-size: 10.5px; line-height: 14px;
  }
  .label__weight {
    position: absolute; right: 18px; top: 112px; text-align: center;
    font-weight: 500; font-size: 9.5px; line-height: 11.5px;
  }
</style>
</head>
<body>
<main class="range">

  <section class="pouch pouch--culinary">
    <div class="leaf-art" role="img" aria-label="Illustration of fresh green tea leaves"></div>
    <div class="brand"><span class="brand__mark"></span><div class="brand__name">TEA KANOSEKI</div></div>
    <div class="verse verse--main">津喜先生谊喜</div>
    <div class="verse verse--side">来生由时西生</div>
    <div class="grade">CULINARY</div>
    <p class="uses">LATTES, SMOOTHIES,<br>BAKING, HOT OR<br>COLD SHOTS</p>
    <div class="badges"><span class="badge--round"></span><span class="badge--oval"></span><span class="badge--plate"></span></div>
    <div class="label">
      <p class="label__name">SINGLE<br>CULTIVA<br>OKUMIDORI</p>
      <p class="label__tagline">A naturally potent boost<br>for body mind and spirit</p>
      <p class="label__weight">Net weight<br>3.52oz (100g)</p>
    </div>
  </section>

  <section class="pouch pouch--premium">
    <div class="leaf-art" role="img" aria-label="Illustration of fresh green tea leaves"></div>
    <div class="brand"><span class="brand__mark"></span><div class="brand__name">TEA KANOSEKI</div></div>
    <div class="verse verse--main">津喜先生谊喜</div>
    <div class="verse verse--side">来生由时西生</div>
    <div class="grade">PREMIUM</div>
    <p class="uses">LATTES, SMOOTHIES,<br>BAKING, HOT OR<br>COLD SHOTS</p>
    <div class="badges"><span class="badge--round"></span><span class="badge--oval"></span><span class="badge--plate"></span></div>
    <div class="label">
      <p class="label__name">SINGLE<br>CULTIVA<br>OKUMIDORI</p>
      <p class="label__tagline">A naturally potent boost<br>for body mind and spirit</p>
      <p class="label__weight">Net weight<br>3.52oz (100g)</p>
    </div>
  </section>

  <section class="pouch pouch--ceremonial">
    <div class="leaf-art" role="img" aria-label="Illustration of fresh green tea leaves"></div>
    <div class="brand"><span class="brand__mark"></span><div class="brand__name">TEA KANOSEKI</div></div>
    <div class="verse verse--main">津喜先生谊喜</div>
    <div class="verse verse--side">来生由时西生</div>
    <div class="grade">CEREMONIAL</div>
    <p class="uses">LATTES, SMOOTHIES,<br>BAKING, HOT OR<br>COLD SHOTS</p>
    <div class="badges"><span class="badge--round"></span><span class="badge--oval"></span><span class="badge--plate"></span></div>
    <div class="label">
      <p class="label__name">SINGLE<br>CULTIVA<br>OKUMIDORI</p>
      <p class="label__tagline">A naturally potent boost<br>for body mind and spirit</p>
      <p class="label__weight">Net weight<br>3.52oz (100g)</p>
    </div>
  </section>

</main>
</body>
</html>
```